Designer brand for needs a banner design

Kavyalok Designs is a designer brand for bed sheets, bed spreads, table runners, hand bags and accessories. Our web site is at www.kavyalokdesigns.example. Details and sample product designs can be found at our site for ideas.

We need a horizontal and vertical banner (different designs) for use in trade shows. Possible 4' x 6' (horizontal design) and 6' x 4' (vertical design).

Banner should include company name, web site, email address (sales@kavyalokdesigns.example), logo, and some background pictures/graphics, etc. Physical address should not be entered in the banner.

Requirements
Must have
• At-least one picture of a bed spread from our web site. See bed spread collections at www.kavyalokdesigns.example
Should not have
• Physical mailing address

```html
<!DOCTYPE html>
<html lang="en">
<head>
<meta charset="utf-8">
<title>Kavyalok Designs – Vertical Banner</title>
<link rel="stylesheet" href="https://fonts.googleapis.com/css2?family=Great+Vibes&family=Open+Sans:wght@400&display=swap">
<style>
  :root {
    --ink-dark: #0b0a0a;
    --backdrop: #1b1a14;
    --cushion-maroon: #4a1428;
    --cushion-maroon-light: #5e1c33;
    --cushion-purple: #2c1d3c;
    --cushion-green: #2f3a1e;
    --cushion-olive: #4a4420;
    --cushion-olive-dark: #2e2a14;
    --text-white: #f4f1ee;
    --text-soft: #d9d4cf;
    --accent-orange: #f08a1e;
    --mark-box: rgba(70, 30, 42, 0.9);
    --mark-edge: rgba(150, 140, 140, 0.55);
  }
  html, body {
    margin: 0;
    padding: 0;
    overflow: hidden;
    background: var(--ink-dark);
  }
  .banner {
    position: relative;
    width: 800px;
    height: 1200px;
    overflow: hidden;
    background: linear-gradient(180deg, var(--backdrop) 0%, var(--backdrop) 60%, var(--ink-dark) 85%);
  }
  .cushion-photo {
    position: absolute;
    inset: 0;
    width: 800px;
    height: 1200px;
  }
  .brand-mark {
    position: absolute;
    top: 245px;
    left: 315px;
    width: 170px;
    height: 150px;
    box-sizing: border-box;
    border: 2px solid var(--mark-edge);
    border-radius: 8px;
    background: var(--mark-box);
  }
  .brand-name {
    position: absolute;
    top: 420px;
    left: 0;
    width: 100%;
    margin: 0;
    text-align: center;
    font-family: "Great Vibes", cursive;
    font-weight: 400;
    font-size: 92px;
    line-height: 1.2;
    color: var(--text-white);
  }
  .contact {
    position: absolute;
    top: 1040px;
    left: 0;
    width: 100%;
    display: flex;
    flex-direction: column;
    align-items: center;
    gap: 14px;
    font-family: "Open Sans", sans-serif;
    font-size: 26px;
    color: var(--text-soft);
  }
  .contact__item {
    display: flex;
    align-items: center;
    gap: 16px;
  }
  .contact__icon {
    width: 24px;
    height: 24px;
    flex: none;
  }
</style>
</head>
<body>
  <main class="banner">
    <svg class="cushion-photo" viewBox="0 0 800 1200" role="img" aria-label="Dimmed photograph of stacked cushions: a maroon cushion with purple embroidered trim, and an olive mirror-work embroidered cushion in front">
      <defs>
        <linearGradient id="maroonFill" x1="0" y1="0" x2="1" y2="1">
          <stop offset="0" stop-color="var(--cushion-maroon-light)"/>
          <stop offset="1" stop-color="var(--cushion-maroon)"/>
        </linearGradient>
        <linearGradient id="oliveFill" x1="0" y1="0" x2="1" y2="1">
          <stop offset="0" stop-color="var(--cushion-olive)"/>
          <stop offset="1" stop-color="var(--cushion-olive-dark)"/>
        </linearGradient>
        <linearGradient id="fadeOut" x1="0" y1="0" x2="0" y2="1">
          <stop offset="0.6" stop-color="var(--ink-dark)" stop-opacity="0"/>
          <stop offset="0.85" stop-color="var(--ink-dark)" stop-opacity="1"/>
        </linearGradient>
      </defs>
      <path d="M0 170 Q250 120 540 140 L600 180 L0 260 Z" fill="var(--cushion-purple)"/>
      <path d="M600 340 Q720 300 800 320 L800 640 Q700 600 620 560 Z" fill="var(--cushion-green)"/>
      <path d="M0 200 Q300 150 650 130 Q690 300 640 560 Q330 610 0 700 Z" fill="url(#maroonFill)"/>
      <path d="M130 555 Q450 530 800 510 L800 960 Q450 990 170 980 Q110 760 130 555 Z" fill="url(#oliveFill)"/>
      <rect x="0" y="0" width="800" height="1200" fill="url(#fadeOut)"/>
    </svg>

    <div class="brand-mark" aria-hidden="true"></div>

    <h1 class="brand-name">Kavyalok Designs</h1>

    <div class="contact">
      <div class="contact__item">
        <svg class="contact__icon" viewBox="0 0 24 24" aria-hidden="true">
          <rect x="2" y="5" width="20" height="14" rx="1.5" fill="var(--accent-orange)"/>
          <path d="M2.5 6 L12 13 L21.5 6" fill="none" stroke="var(--ink-dark)" stroke-width="1.6"/>
        </svg>
        <span>sales@kavyalokdesigns.example</span>
      </div>
      <div class="contact__item">
        <svg class="contact__icon" viewBox="0 0 24 24" aria-hidden="true">
          <g fill="none" stroke="var(--accent-orange)" stroke-width="2.6" stroke-linecap="round">
            <path d="M10 14 L14 10"/>
            <path d="M8.5 11 L6 13.5 a3.5 3.5 0 0 0 5 5 L13.5 16"/>
            <path d="M15.5 13 L18 10.5 a3.5 3.5 0 0 0 -5 -5 L10.5 8"/>
          </g>
        </svg>
        <span>www.kavyalokdesigns.example</span>
      </div>
    </div>
  </main>
</body>
</html>
```